Author/ Speaker Business Card design

I need a business card designed that will go with the branding that is already on my book and website. I like clean and straightforward, but I am not opposed to something more 'innovative'.

Target Market(s)

Colleges and Universities, educational institutions

Industry/Entity Type

Education

Contact Information for Business Card

Standard size. It should be able to be printed on good quality white or ivory paper.

Font styles to use
Sans Serif

Colors
0355a3

Requirements
Must have
• There's a blue on my website. It should have some blue. My logo is at the top. It should have the logo incorporated somewhere on it. My name, Author | Speaker | Teacher | Trainer, my phone number (+31 64-207 5819), my email address (milo@theboldlearner.example), Social media icons (twitter, Instagram, LinkedIn) with the addresses (twitter @writermilofenwick, Instagram - theboldlearner, LinkedIn - theboldlearner) By they way, the website is www.theboldlearner.example. There is a photo of the book on the website. Also, my full name is Milo Fenwick
Nice to have
• Try to use the font that is on the website and book. Also, if you could get that blue, that would be great.
Should not have
• My photo

```html
<!DOCTYPE html>
<html lang="en">
<head>
<meta charset="utf-8">
<title>Milo Fenwick – Business Card</title>
<link rel="stylesheet" href="https://fonts.googleapis.com/css2?family=Lato:wght@400;700;900&display=swap">
<style>
  :root {
    --brand-blue: #0355a3;
    --paper: #ffffff;
    --ink: #1d1d1f;
    --backdrop: #e6e7ea;
  }
  * { box-sizing: border-box; margin: 0; padding: 0; }
  html, body {
    width: 1200px; height: 1059px; overflow: hidden;
    background: var(--backdrop);
    font-family: "Lato", sans-serif;
  }
  .sheet { position: relative; width: 1200px; height: 1059px; }
  .card {
    position: absolute; left: 250px; width: 700px; height: 400px;
    overflow: hidden;
    box-shadow: 0 10px 30px rgba(0,0,0,.18);
  }
  .brand-name {
    font-weight: 900; letter-spacing: -0.5px; line-height: 1;
    display: flex; align-items: center; gap: 14px;
    white-space: nowrap;
  }
  .brand-name__mark { width: 22px; height: 22px; border-radius: 50%; flex: none; }

  /* Front */
  .card--front {
    top: 90px; background: var(--brand-blue);
    display: flex; align-items: center; justify-content: center;
  }
  .front-lockup { display: flex; flex-direction: column; align-items: flex-end; gap: 18px; }
  .card--front .brand-name { color: var(--paper); font-size: 44px; }
  .card--front .brand-name__mark { background: var(--paper); }
  .front-url {
    color: var(--paper); font-size: 17px; letter-spacing: 1px; white-space: nowrap;
  }

  /* Back */
  .card--back { top: 570px; background: var(--paper); }
  .card--back .brand-name {
    position: absolute; left: 48px; top: 180px;
    color: var(--brand-blue); font-size: 36px;
  }
  .card--back .brand-name__mark { background: var(--brand-blue); }
  .divider {
    position: absolute; left: 375px; top: 85px; width: 2px; height: 215px;
    background: var(--brand-blue);
  }
  .details { position: absolute; left: 400px; top: 78px; color: var(--ink); }
  .details__name {
    color: var(--brand-blue); font-weight: 900; font-size: 27px; line-height: 1.1;
  }
  .details__roles { font-size: 15px; margin-top: 4px; }
  .contact-list { list-style: none; margin-top: 16px; }
  .contact-list li {
    display: flex; align-items: center; gap: 10px;
    font-size: 15.5px; line-height: 24px;
  }
  .contact-list svg { width: 14px; height: 14px; flex: none; fill: var(--brand-blue); }
  .social-list { list-style: none; margin-top: 18px; }
  .social-list li {
    display: flex; align-items: center; gap: 10px;
    font-size: 16px; line-height: 24px;
  }
  .social-list__dot {
    width: 12px; height: 12px; background: var(--brand-blue); flex: none; border-radius: 2px;
  }
  .base-band {
    position: absolute; left: 0; bottom: 0; width: 100%; height: 14px;
    background: var(--brand-blue);
  }
</style>
</head>
<body>
<main class="sheet">
  <section class="card card--front">
    <div class="front-lockup">
      <div class="brand-name"><span class="brand-name__mark"></span>The Bold Learner</div>
      <p class="front-url">www.theboldlearner.example</p>
    </div>
  </section>

  <section class="card card--back">
    <div class="brand-name"><span class="brand-name__mark"></span>The Bold Learner</div>
    <div class="divider"></div>
    <div class="details">
      <h1 class="details__name">Milo Fenwick</h1>
      <p class="details__roles">Author | Speaker | Teacher | Trainer</p>
      <ul class="contact-list">
        <li>
          <svg viewBox="0 0 24 24" aria-hidden="true"><path d="M6.6 10.8a15.1 15.1 0 0 0 6.6 6.6l2.2-2.2a1 1 0 0 1 1-.25 11.4 11.4 0 0 0 3.6.57 1 1 0 0 1 1 1V20a1 1 0 0 1-1 1A17 17 0 0 1 3 4a1 1 0 0 1 1-1h3.5a1 1 0 0 1 1 1c0 1.25.2 2.45.57 3.57a1 1 0 0 1-.25 1z"/></svg>
          +31 64-207 5819
        </li>
        <li>
          <svg viewBox="0 0 24 24" aria-hidden="true"><path d="M2 5h20v14H2zm2 2v.4l8 5 8-5V7l-8 5z"/></svg>
          milo@theboldlearner.example
        </li>
        <li>
          <svg viewBox="0 0 24 24" aria-hidden="true"><path d="M12 2a10 10 0 1 0 0 20 10 10 0 0 0 0-20zm6.9 6h-2.9a15.6 15.6 0 0 0-1.4-3.6A8 8 0 0 1 18.9 8zM12 4c.8 1.2 1.5 2.5 1.9 4h-3.8c.4-1.5 1.1-2.8 1.9-4zM4.3 14a8 8 0 0 1 0-4h3.4a16 16 0 0 0 0 4zm.8 2h2.9c.3 1.3.8 2.5 1.4 3.6A8 8 0 0 1 5.1 16zM8 8H5.1a8 8 0 0 1 4.3-3.6C8.8 5.5 8.3 6.7 8 8zm4 12c-.8-1.2-1.5-2.5-1.9-4h3.8c-.4 1.5-1.1 2.8-1.9 4zm2.3-6H9.7a14.7 14.7 0 0 1 0-4h4.6a14.7 14.7 0 0 1 0 4zm.3 5.6c.6-1.1 1.1-2.3 1.4-3.6h2.9a8 8 0 0 1-4.3 3.6zM16.3 14a16 16 0 0 0 0-4h3.4a8 8 0 0 1 0 4z"/></svg>
          www.theboldlearner.example
        </li>
      </ul>
      <ul class="social-list">
        <li><span class="social-list__dot"></span>@writermilofenwick</li>
        <li><span class="social-list__dot"></span>theboldlearner</li>
      </ul>
    </div>
    <div class="base-band"></div>
  </section>
</main>
</body>
</html>
```